NEW Way Out Rooms. Fun, Dark and Mysterious.

Way Out Rooms Website. Bookings and scheduling of appointments will be organised with Bookvane through the site. Most appointments will be created online through the booking system with some payments coming through in person by drop-ins. Groups will be from 2 - 8 people with a sliding scale of prices. We will start with one game playable and one saying coming soon. We will also eventually have 4 games up and running at once so will need it to be able to expand. We don't have any images of the rooms because it all relies heavily on mystery. Appointments are each 1 hour long with 30 minutes in between.

Target Market(s)

15-35 year olds

Coding

Coded - Design and coding required

Number of Pages Required

5+ page

Font styles to use
Decorative

Colors

Designer to choose colors to be used in the design.

Requirements
Must have
• Graphics showing what an Way Out Rooms is.
• Page for About - What is an Way Out Rooms
• Page for Games - Showing each of the different games which can be played with links to booking page. We have one game to start - the surgeons shadows. A victorian doctors office and serial killers. Then a game coming soon which is aztec/mayan/jungle/harold Crane feel.
• FAQ Page
Nice to have
• Graphics for multiple players ie 2 players, 3 players, 4 players etc
• Dark and Mysterious feel.
• Inspiration from Puzzle Vault, Cipher Lodge, Quest Lockbox
Should not have
• Cartoony/childish. Pink.
• Not bloody or dripping letters etc - not cliche.
• Not horror themed.

```html
<!DOCTYPE html>
<html lang="en">
<head>
<meta charset="utf-8">
<title>The Way Out — Escape Room Experience</title>
<link rel="stylesheet" href="https://fonts.googleapis.com/css2?family=Bree+Serif&family=Nunito+Sans:wght@400;600;700;800&display=swap">
<style>
:root{
  --gold:#e2bb5c;
  --amber:#c98a3e;
  --rust:#b4652f;
  --orange:#c9722e;
  --ink:#1b1b1b;
  --muted:#8a8a8a;
  --line:#e6e6e6;
  --soft:#f4f4f4;
  --footer:#1d1a16;
  --grad:linear-gradient(90deg,var(--gold),var(--rust));
}
*{box-sizing:border-box;margin:0;padding:0}
html,body{width:1200px;height:4501px;overflow:hidden}
body{position:relative;background:#fff;font-family:"Nunito Sans",sans-serif;color:var(--ink)}
.abs{position:absolute}
.display{font-family:"Bree Serif",serif}
.eyebrow{font-size:11px;font-weight:800;color:var(--orange);letter-spacing:.3px;text-transform:uppercase}
.copy{font-size:11.5px;line-height:21px;color:var(--muted)}
.btn{position:absolute;display:flex;align-items:center;justify-content:center;background:var(--grad);color:#fff;font-family:"Bree Serif",serif;font-size:15px;border-radius:4px;box-shadow:0 6px 14px rgba(180,101,47,.25)}
.photo{position:absolute;border-radius:22px;overflow:hidden}
.dots{position:absolute;background-image:radial-gradient(circle,#c9c9c9 1.4px,transparent 1.6px);background-size:14px 14px}
.frame{position:absolute;border:2px solid var(--gold);border-radius:20px}
.center{text-align:center;left:0;width:1200px}

.hero-shape{left:748px;top:0;width:452px;height:568px;background:linear-gradient(135deg,#e6c070,#d09a43);border-bottom-left-radius:60px}
.logo{left:161px;top:22px;display:flex;align-items:center;gap:6px;font-family:"Bree Serif",serif;font-size:15px;color:var(--ink)}
.logo i{width:12px;height:12px;border-radius:50%;background:var(--amber)}
.nav a{position:absolute;top:41px;font-size:12px;font-weight:700;color:var(--ink);text-decoration:none}
.nav .book{color:#fff;font-family:"Bree Serif",serif;font-size:15px;text-decoration:underline;top:37px}
.pager span{position:absolute;left:68px;width:9px;height:9px;border:1.5px solid #9a9a9a}
.pager .on{background:var(--orange);border-color:var(--orange);transform:rotate(45deg)}

.step-icon{position:absolute;left:161px;width:61px;height:61px;border-radius:10px;background:#fff;box-shadow:0 4px 14px rgba(0,0,0,.1);display:flex;align-items:center;justify-content:center}
.step-title{position:absolute;left:238px;font-family:"Bree Serif",serif;font-size:12px}
.step-copy{position:absolute;left:238px;font-size:11px;color:var(--muted)}

.band{left:0;top:1544px;width:1200px;height:474px;background:linear-gradient(90deg,#e5c062,#b86a34)}
.style-card{position:absolute;top:1703px;width:203px;height:231px;background:#fff;border-radius:8px;text-align:center;box-shadow:0 8px 20px rgba(0,0,0,.12)}
.style-card svg{margin-top:30px}
.style-card h3{font-family:"Bree Serif",serif;font-weight:400;font-size:15px;margin-top:10px}
.style-card p{font-size:10.5px;line-height:21px;color:var(--muted);padding:4px 8px 0}
.more{font-size:11px;font-weight:800;color:var(--orange);text-decoration:underline}
.style-card .more{display:block;margin-top:7px}

.price{position:absolute;width:68px;height:66px;background:var(--amber);border:2px solid #fff;border-radius:4px;color:#fff;text-align:center;font-size:10px;line-height:12px;padding-top:8px}
.price b{display:block;font-family:"Bree Serif",serif;font-size:20px;line-height:22px;font-weight:400}
.game-card{position:absolute;width:451px;height:300px;background:#fff;border-radius:10px;box-shadow:0 6px 24px rgba(0,0,0,.1);text-align:center}
.game-card h3{font-family:"Bree Serif",serif;font-weight:400;font-size:17px;margin-top:36px}
.game-card p{font-size:11px;line-height:21px;color:var(--muted);width:380px;margin:8px auto 0}
.facts{display:flex;justify-content:center;gap:46px;margin-top:12px}
.facts div{font-size:10.5px;color:#333;width:80px}
.facts svg{display:block;margin:0 auto 6px}
.game-card .btn{position:relative;margin:22px auto 0;width:112px;height:35px;font-size:13px}

.soft{left:0;top:3071px;width:1200px;height:622px;background:var(--soft)}
.tile-title{position:absolute;font-family:"Bree Serif",serif;font-size:14px;top:3494px}
.tile-copy{position:absolute;top:3521px;width:200px;font-size:10.5px;line-height:21px;color:var(--muted)}
.tile-more{position:absolute;top:3590px}

.field{position:absolute;background:var(--soft);border:1px solid #e9e9e9;border-radius:4px;font-size:10px;color:#9a9a9a;padding:11px 15px}

.footer{left:0;top:4167px;width:1200px;height:334px;background:radial-gradient(ellipse at 40% 40%,#2c261e,var(--footer))}
.f-head{position:absolute;top:4234px;font-family:"Bree Serif",serif;font-size:15px;color:var(--gold)}
.f-list{position:absolute;top:4292px;list-style:none;font-size:10.5px;line-height:21px;color:#ddd}
.f-text{position:absolute;font-size:10.5px;line-height:21px;color:#ddd}
.social span{position:absolute;top:4397px;width:36px;height:36px;border:1.5px solid var(--gold);border-radius:3px}
.social .on{background:var(--amber)}
</style>
</head>
<body>

<div class="abs hero-shape"></div>
<div class="abs logo"><i></i>Way Out</div>
<nav class="nav">
  <a style="left:554px">Home</a>
  <a style="left:618px">About Us</a>
  <a style="left:701px">Game</a>
  <a style="left:769px">FAQ's</a>
  <a style="left:835px">Contact Us</a>
  <a class="book" style="left:945px">Book Now</a>
</nav>
<div class="photo" role="img" aria-label="Two players peeking out of a round vault door" style="left:589px;top:80px;width:563px;height:421px;background:linear-gradient(135deg,#2a1d2c,#5b3a30 50%,#8a6a4a)"></div>
<div class="dots" style="left:663px;top:503px;width:84px;height:54px"></div>
<div class="pager"><span style="top:209px"></span><span style="top:255px"></span><span class="on" style="top:302px"></span><span style="top:351px"></span></div>

<div class="abs eyebrow" style="left:162px;top:199px;font-size:12px">Escape Room Experience</div>
<h1 class="abs display" style="left:160px;top:218px;font-size:58px;font-weight:400;line-height:70px">The Way Out</h1>
<p class="abs copy" style="left:162px;top:289px;width:395px;font-size:12px;line-height:22px">Lorem Ipsum is simply dummy text of the printing and typesetting industry. Lorem Ipsum has been the industry's standard dummy text ever since the 1500s.</p>
<div class="btn" style="left:162px;top:402px;width:224px;height:51px;font-size:16px">Book An Appointment</div>

<div class="dots" style="left:118px;top:734px;width:36px;height:136px"></div>
<div class="frame" style="left:299px;top:700px;width:226px;height:264px"></div>
<div class="photo" role="img" aria-label="Candle-lit library room with a player searching the shelves" style="left:161px;top:676px;width:337px;height:262px;background:linear-gradient(120deg,#3a1608,#8a3a12 40%,#1c1426)"></div>
<div class="abs eyebrow" style="left:627px;top:688px">About Us</div>
<h2 class="abs display" style="left:627px;top:706px;font-size:32px;font-weight:400">The Way Out</h2>
<p class="abs copy" style="left:627px;top:755px;width:290px">Lorem Ipsum is simply dummy text of the printing and typesetting industry. Lorem Ipsum has been the industry's standard dummy text ever since the 1500s, when an unknown printer took a galley of type and scrambled it to make a type specimen book. It has survived not only five centuries, but also the leap into electronic typesetting, remaining essentially unchanged.</p>
<div class="btn" style="left:627px;top:928px;width:112px;height:35px;font-size:13px">Book Now</div>

<div class="abs eyebrow" style="left:162px;top:1058px">Our Work</div>
<h2 class="abs display" style="left:162px;top:1076px;font-size:32px;font-weight:400">How Its Work</h2>
<p class="abs copy" style="left:162px;top:1122px;width:345px">Lorem Ipsum is simply dummy text of the printing and typesetting industry. Lorem Ipsum has been the industry's standard dummy text ever since the 1500s.</p>

<div class="step-icon" style="top:1218px"><svg width="36" height="32" viewBox="0 0 36 32" fill="none" stroke="#c9722e" stroke-width="1.5"><circle cx="7" cy="6" r="3"/><circle cx="18" cy="6" r="3"/><circle cx="29" cy="6" r="3"/><path d="M3 30V14h8v16M14 30V14h8v16M25 30V14h8v16"/></svg></div>
<div class="step-title" style="top:1228px">2 to 6 Players</div>
<div class="step-copy" style="top:1250px">Lorem Ipsum is simply dummy text.</div>

<div class="step-icon" style="top:1302px"><svg width="30" height="32" viewBox="0 0 30 32" fill="none" stroke="#c9722e" stroke-width="1.5"><circle cx="15" cy="18" r="12"/><path d="M15 18V11M12 3h6M15 3v3"/></svg></div>
<div class="step-title" style="top:1312px">45 minutes of Game Play</div>
<div class="step-copy" style="top:1334px">Lorem Ipsum is simply dummy text.</div>

<div class="step-icon" style="top:1382px"><svg width="34" height="30" viewBox="0 0 34 30" fill="none" stroke="#c9722e" stroke-width="1.5"><path d="M3 14L17 3l14 11M7 11v16h20V11"/><circle cx="14" cy="19" r="3"/><path d="M17 19h6v3"/></svg></div>
<div class="step-title" style="top:1393px">Tons of Adventures to choose From</div>
<div class="step-copy" style="top:1415px">Lorem Ipsum is simply dummy text.</div>

<div class="frame" style="left:617px;top:1279px;width:150px;height:186px"></div>
<div class="photo" role="img" aria-label="Players solving clues in a dim red-walled kitchen room" style="left:639px;top:1069px;width:376px;height:374px;background:linear-gradient(140deg,#4a1a14,#7a3420 45%,#2a2118)"></div>
<div class="dots" style="left:1020px;top:1186px;width:40px;height:144px"></div>

<div class="abs band"></div>
<div class="abs center eyebrow" style="top:1606px;color:#fff;font-size:10px">Step To Follow</div>
<h2 class="abs center display" style="top:1624px;font-size:30px;font-weight:400;color:#fff">Game Style</h2>

<div class="style-card" style="left:161px">
  <svg width="46" height="46" viewBox="0 0 46 46" fill="none" stroke="#c9722e" stroke-width="1.6"><rect x="4" y="4" width="24" height="24" rx="2"/><path d="M10 16l5 5 10-12"/><rect x="18" y="20" width="24" height="22" rx="2"/><path d="M24 31l4 4 9-9"/></svg>
  <h3>Tasks</h3><p>Lorem Ipsum is simply dummy text of the printing and typesetting industry. Lorem Ipsum has been the.</p><span class="more">Read More</span>
</div>
<div class="style-card" style="left:386px">
  <svg width="46" height="46" viewBox="0 0 46 46" fill="none" stroke="#c9722e" stroke-width="1.6"><circle cx="19" cy="19" r="15"/><path d="M19 10v9l6 4"/><ellipse cx="36" cy="28" rx="7" ry="3"/><path d="M29 28v12c0 2 14 2 14 0V28M29 34c0 2 14 2 14 0"/></svg>
  <h3>Time</h3><p>Lorem Ipsum is simply dummy text of the printing and typesetting industry. Lorem Ipsum has been the.</p><span class="more">Read More</span>
</div>
<div class="style-card" style="left:611px">
  <svg width="46" height="46" viewBox="0 0 46 46" fill="none" stroke="#c9722e" stroke-width="1.6"><path d="M6 10h10a4 4 0 118 0h10v10a4 4 0 110 8v10H24a4 4 0 10-8 0H6V28a4 4 0 100-8z"/></svg>
  <h3>Command</h3><p>Lorem Ipsum is simply dummy text of the printing and typesetting industry. Lorem Ipsum has been the.</p><span class="more">Read More</span>
</div>
<div class="style-card" style="left:837px">
  <svg width="46" height="46" viewBox="0 0 46 46" fill="none" stroke="#c9722e" stroke-width="1.6"><circle cx="23" cy="23" r="20"/><circle cx="23" cy="23" r="14"/><circle cx="23" cy="19" r="4"/><path d="M16 31c2-5 12-5 14 0"/></svg>
  <h3>Impression</h3><p>Lorem Ipsum is simply dummy text of the printing and typesetting industry. Lorem Ipsum has been the.</p><span class="more">Read More</span>
</div>

<div class="abs center eyebrow" style="top:2094px;font-size:10px">Games</div>
<h2 class="abs center display" style="top:2111px;font-size:30px;font-weight:400">Our Games</h2>

<div class="dots" style="left:102px;top:2280px;width:52px;height:142px"></div>
<div class="photo" role="img" aria-label="Player in a blue-lit corridor room" style="left:161px;top:2203px;width:487px;height:299px;border-radius:14px;background:linear-gradient(120deg,#0f2a44,#1f4e74 50%,#0a1a2c)"></div>
<div class="price" style="left:171px;top:2212px"><b>$ 56</b>Per<br>Person</div>
<div class="game-card" style="left:461px;top:2255px">
  <h3>Surgeons Shadows</h3>
  <p>Lorem ipsum is simply dummy text of the printing and typesetting industry. Lorem Ipsum has been the industry's standard dummy text ever since the 1500s.</p>
  <div class="facts">
    <div><svg width="24" height="22" viewBox="0 0 24 22" fill="none" stroke="#d9a24a" stroke-width="1.3"><path d="M2 20l5-14 5 4 5-6 5 16z"/><circle cx="12" cy="6" r="2.5"/></svg>12 Lantern Lane</div>
    <div><svg width="26" height="22" viewBox="0 0 26 22" fill="none" stroke="#d9a24a" stroke-width="1.3"><circle cx="8" cy="6" r="3"/><circle cx="18" cy="6" r="3"/><path d="M2 20c0-6 12-6 12 0M12 20c0-6 12-6 12 0"/></svg>2 - 4 People</div>
    <div><svg width="16" height="22" viewBox="0 0 16 22" fill="none" stroke="#d9a24a" stroke-width="1.3"><path d="M2 1h12M2 21h12M3 1c0 7 10 7 10 10S3 14 3 21M13 1c0 7-10 7-10 10s10 3 10 10"/></svg>60 Minutes</div>
  </div>
  <div class="btn">Choose Game</div>
</div>

<div class="dots" style="left:1046px;top:2716px;width:52px;height:142px"></div>
<div class="photo" role="img" aria-label="Two players examining clues in a brick-walled study" style="left:550px;top:2636px;width:489px;height:300px;border-radius:14px;background:linear-gradient(120deg,#2e2520,#6a4a38 50%,#241d1a)"></div>
<div class="price" style="left:963px;top:2647px"><b>$ 56</b>Per<br>Person</div>
<div class="game-card" style="left:288px;top:2689px">
  <h3>Jaguar King's Tomb</h3>
  <p>Lorem ipsum is simply dummy text of the printing and typesetting industry. Lorem Ipsum has been the industry's standard dummy text ever since the 1500s.</p>
  <div class="facts">
    <div><svg width="24" height="22" viewBox="0 0 24 22" fill="none" stroke="#d9a24a" stroke-width="1.3"><path d="M2 20l5-14 5 4 5-6 5 16z"/><circle cx="12" cy="6" r="2.5"/></svg>12 Lantern Lane</div>
    <div><svg width="26" height="22" viewBox="0 0 26 22" fill="none" stroke="#d9a24a" stroke-width="1.3"><circle cx="8" cy="6" r="3"/><circle cx="18" cy="6" r="3"/><path d="M2 20c0-6 12-6 12 0M12 20c0-6 12-6 12 0"/></svg>2 - 4 People</div>
    <div><svg width="16" height="22" viewBox="0 0 16 22" fill="none" stroke="#d9a24a" stroke-width="1.3"><path d="M2 1h12M2 21h12M3 1c0 7 10 7 10 10S3 14 3 21M13 1c0 7-10 7-10 10s10 3 10 10"/></svg>60 Minutes</div>
  </div>
  <div class="btn">Choose Game</div>
</div>

<div class="abs soft"></div>
<div class="abs center eyebrow" style="top:3144px;font-size:10px">Games</div>
<h2 class="abs center display" style="top:3162px;font-size:30px;font-weight:400">Our Games</h2>

<div class="photo" role="img" aria-label="Family gathered around candles at a table" style="left:232px;top:3251px;width:225px;height:225px;border-radius:14px;background:linear-gradient(135deg,#d8b06a,#7a3a1a 60%,#2a140a)"></div>
<div class="tile-title" style="left:245px">Family</div>
<p class="tile-copy" style="left:245px">Lorem ipsum is simply dummy text of the printing and typesetting industry. Lorem Ipsum has been the.</p>
<span class="more tile-more" style="left:245px">Read More</span>

<div class="photo" role="img" aria-label="Group of friends standing outdoors" style="left:487px;top:3251px;width:225px;height:225px;border-radius:14px;background:linear-gradient(160deg,#b8c0c4,#5a5f60 55%,#2c2a28)"></div>
<div class="tile-title" style="left:500px">Friends</div>
<p class="tile-copy" style="left:500px">Lorem ipsum is simply dummy text of the printing and typesetting industry. Lorem Ipsum has been the.</p>
<span class="more tile-more" style="left:500px">Read More</span>

<div class="photo" role="img" aria-label="Colleagues working together around an office table" style="left:742px;top:3251px;width:225px;height:225px;border-radius:14px;background:linear-gradient(140deg,#2b3a3a,#8a8f86 55%,#3a3530)"></div>
<div class="tile-title" style="left:755px">Corporate</div>
<p class="tile-copy" style="left:755px">Lorem ipsum is simply dummy text of the printing and typesetting industry. Lorem Ipsum has been the.</p>
<span class="more tile-more" style="left:755px">Read More</span>

<div class="abs center eyebrow" style="top:3747px;font-size:10px">Get In Touch</div>
<h2 class="abs center display" style="top:3764px;font-size:30px;font-weight:400">Are Ready To Play Game?</h2>
<div class="field" style="left:398px;top:3836px;width:194px;height:37px">Name:</div>
<div class="field" style="left:606px;top:3836px;width:196px;height:37px">Phone:</div>
<div class="field" style="left:398px;top:3889px;width:404px;height:37px">Email:</div>
<div class="field" style="left:398px;top:3943px;width:404px;height:73px">Message:</div>
<div class="btn" style="left:494px;top:4055px;width:210px;height:37px;font-size:14px">Schedule An Appointment</div>

<div class="abs footer"></div>
<div class="abs logo" style="left:166px;top:4240px;color:var(--gold)"><i></i>Way Out</div>
<p class="f-text" style="left:162px;top:4298px;width:210px">Lorem Ipsum is simply dummy text of the printing and typesetting industry. Lorem Ipsum has been the industry's standard dummy text ever since the 1500s.</p>
<div class="social"><span style="left:161px"></span><span class="on" style="left:206px"></span><span style="left:251px"></span><span style="left:297px"></span></div>

<div class="f-head" style="left:388px">Quick Links</div>
<ul class="f-list" style="left:388px"><li>Home</li><li>About Us</li><li>Games</li><li>FAQ's</li><li>Contact Us</li></ul>

<div class="f-head" style="left:611px">Game Styles</div>
<ul class="f-list" style="left:611px"><li>Tastks</li><li>Time</li><li>Commands</li><li>Impressions</li></ul>

<div class="f-head" style="left:837px">Contact Info</div>
<svg class="abs" style="left:840px;top:4289px" width="22" height="22" viewBox="0 0 22 22" fill="none" stroke="#e2bb5c" stroke-width="1.5"><path d="M5 2l4 4-2 3c1 3 3 5 6 6l3-2 4 4-3 3C10 20 2 12 2 5z"/></svg>
<div class="f-text" style="left:875px;top:4289px">+1-555-014-2290</div>
<svg class="abs" style="left:838px;top:4336px" width="24" height="18" viewBox="0 0 24 18" fill="none" stroke="#e2bb5c" stroke-width="1.5"><rect x="1" y="1" width="22" height="16" rx="1"/><path d="M1 1l11 9 11-9"/></svg>
<div class="f-text" style="left:875px;top:4333px">hello@wayoutrooms.test</div>
<svg class="abs" style="left:841px;top:4380px" width="20" height="26" viewBox="0 0 20 26" fill="none" stroke="#e2bb5c" stroke-width="1.5"><path d="M10 25S2 15 2 9a8 8 0 0116 0c0 6-8 16-8 16z"/><circle cx="10" cy="9" r="3"/></svg>
<div class="f-text" style="left:875px;top:4378px;width:90px">100 lorem ipsum is simply dummy text.</div>

<div class="abs center" style="top:4470px;font-size:10px;color:#ddd">Copyright ©2020 Way Out Rooms. All Right's Reserved. Terms &amp; Conditions</div>

</body>
</html>
```